Brindle Works Ltd

I'd like to create a company letterhead for the attached logo in word format.

I'd like to emphasis the icon in large translucent state from the left corner and ensure that the letterhead colouring matches the colour palette of the current logo with a contrast so it's clear to see. I've attached a copy of our sister company page on the app for reference.

```html
<!DOCTYPE html>
<html lang="en">
<head>
<meta charset="utf-8">
<title>Brindle Works Ltd – Letterhead</title>
<link href="https://fonts.googleapis.com/css2?family=Questrial&family=Arimo:wght@400&display=swap" rel="stylesheet">
<style>
  :root {
    --backdrop: #e3e3e3;
    --paper: #ffffff;
    --brand-teal: #17bfa7;
    --brand-tint: #eef8f8;
    --ink: #555555;
    --ink-soft: #9a9a9a;
    --rule: #cfcfcf;
  }
  html, body {
    margin: 0;
    width: 1200px;
    height: 1200px;
    overflow: hidden;
    background: var(--backdrop);
  }
  .letterhead {
    position: absolute;
    left: 233px;
    top: 81px;
    width: 734px;
    height: 1038px;
    background: var(--paper);
    overflow: hidden;
    font-family: "Arimo", Arial, sans-serif;
    color: var(--ink);
  }
  .backdrop-disc {
    position: absolute;
    left: -137px;
    top: 310px;
    width: 746px;
    height: 746px;
    border-radius: 50%;
    background: var(--brand-tint);
  }
  .brand {
    position: absolute;
    left: 65px;
    top: 58px;
    display: flex;
    align-items: center;
    gap: 10px;
  }
  .brand-dot {
    width: 34px;
    height: 34px;
    border-radius: 50%;
    background: var(--brand-teal);
  }
  .brand-name {
    font-family: "Questrial", Arial, sans-serif;
    font-size: 26px;
    color: var(--brand-teal);
    white-space: nowrap;
  }
  .divider {
    position: absolute;
    top: 57px;
    width: 1px;
    height: 43px;
    background: var(--rule);
  }
  .divider--first { left: 353px; }
  .divider--second { left: 502px; }
  .address, .contacts {
    position: absolute;
    top: 52px;
    margin: 0;
    padding: 0;
    list-style: none;
    font-size: 11px;
    line-height: 16.7px;
    color: var(--ink-soft);
    font-style: normal;
    white-space: nowrap;
  }
  .address { left: 390px; }
  .contacts { left: 537px; }
  .contacts li { display: flex; align-items: center; gap: 6px; }
  .contacts svg { width: 10px; height: 10px; fill: var(--brand-teal); }
  .greeting {
    position: absolute;
    left: 67px;
    top: 318px;
    margin: 0;
    font-family: "Questrial", Arial, sans-serif;
    font-weight: 400;
    font-size: 18.5px;
    -webkit-text-stroke: 0.5px var(--ink);
  }
  .body-copy {
    position: absolute;
    left: 65px;
    top: 367px;
    width: 606px;
  }
  .body-copy p {
    margin: 0 0 13px;
    font-size: 12.7px;
    line-height: 15px;
  }
  .closing {
    position: absolute;
    left: 67px;
    top: 679px;
    margin: 0;
    font-family: "Questrial", Arial, sans-serif;
    font-size: 10px;
    -webkit-text-stroke: 0.3px var(--ink);
  }
  .signature {
    position: absolute;
    left: 85px;
    top: 728px;
    margin: 0;
    font-family: "Questrial", Arial, sans-serif;
    font-size: 18px;
    letter-spacing: -1px;
  }
</style>
</head>
<body>
  <main class="letterhead">
    <div class="backdrop-disc" aria-hidden="true"></div>

    <header>
      <div class="brand">
        <span class="brand-dot" aria-hidden="true"></span>
        <span class="brand-name">Brindle Works Ltd</span>
      </div>
      <span class="divider divider--first"></span>
      <address class="address">
        Your address<br>city<br>state, ZIP 0000
      </address>
      <span class="divider divider--second"></span>
      <ul class="contacts">
        <li>
          <svg viewBox="0 0 10 10" aria-hidden="true"><path d="M2 0.5 L3.6 2.6 L2.8 3.6 Q3.9 5.9 6.3 7.2 L7.4 6.4 L9.5 8 L8.4 9.5 Q3.5 9 0.5 2 Z"/></svg>
          555-014-2290
        </li>
        <li>
          <svg viewBox="0 0 10 10" aria-hidden="true"><path d="M0 2 H10 V8.5 H0 Z M0.8 2.6 L5 5.8 L9.2 2.6 V3.3 L5 6.5 L0.8 3.3 Z" fill-rule="evenodd"/></svg>
          office@brindleworks.example
        </li>
        <li>
          <svg viewBox="0 0 10 10" aria-hidden="true"><circle cx="5" cy="5" r="5"/><path d="M2 3 Q4 2 5 4 Q4 6 3 5 Z M6 6 Q8 5.5 8 7.5 Q6.5 8.5 6 6 Z" fill="#fff"/></svg>
          www.brindleworks.example
        </li>
      </ul>
    </header>

    <h1 class="greeting">Dear Mr. Smith,</h1>

    <section class="body-copy">
      <p>Lorem ipsum dolor sit amet, consectetuer adipiscing elit, sed diam nonmmy nibh euismod tincidunt ut laor eet dolore magna aliquam erat volutpat. Ut wisi enim ad minim veniam, quis nostrud exerci tationmcorper suscipit lobortis nisl ut aliquip ex ea commodo consequat. Duis autem vel eum iriure dolor in hendrerit in vulputate velit esse molestie consequat, vel illum dolore eu feugiat</p>
      <p>Rorem ipsum dolor sit amet, consectetuer adipiscing elit, sed diam nonmmy nibh euismod tincidunt ut laor eet dolore magna aliquam erat volutpat. Ut wisi enim ad minim veniam, quis nostrud exerci tationmcorper suscipit lobortis nisl ut aliquip ex ea commodo consequat. Duis autem vel eum iriure dolor in hendrerit in vulputate velit esse molest</p>
      <p>Dorem ipsum dolor sit amet, consectetuer adipiscing elit, sed diam nonmmy nibh euismod tincidunt ut laor eet dolore magna aliquam erat volutpat. Ut wisi enim ad minim veniam, quis nostrud exerci tationmcorper suscipit lobortis nisl ut aliquip ex ea commodo consequat. Duis autem vel eum iriure dolor in hendrerit in suscipit lobortis nisl ut aliquip ex ea commodo consequat. Duis autem vel eum iriure dolor in hendrerit in vulputate velit esse molestie consequat, vel illum</p>
      <p>Sorem ipsum dolor sit amet, consectetuer adipiscing elit, sed diam nonmmy nibh euismod tincidunt ut laor eet dolore magna aliquam erat volutpat. Ut wisi enim ad minim veniam, quis nostrud exerci tationmcorper suscipit lobortis nisl ut aliquip ex ea commodo consequat. Duis autem vel eum iriure dolor in</p>
    </section>

    <p class="closing">Sincerely,</p>
    <p class="signature">Marten Osby</p>
  </main>
</body>
</html>
```